Looking for an Innovative Print Design (Service Directory)

We need a new design for our advertisement within a printed colour services directory.

We are a compensation law firm called Velbrook Compensation Lawyers. Feel free to take a browse of our website www.velbrooklegal.com.au to get an idea of what we do and the kind of firm we are.

We are in the process of redeveloping our website and as such, so please don't adhere to the design principles of the current site- impress us with your originality!

On top of any editable formats, your final submissions must include a .pdf copy.
The same design will need to be presented in two dimensions:

- 154mm x 118mm (B1/B2 Half Page);
- 175mm x 113mm (B4 Half Page).

[For more information refer to attached Pdf.]

We have attached for you a few examples of other firms' designs (Sample1,2,3). These are by no means good, or what we're after, it's just to provide you with an idea of what sort of advertisements go into the service directory.

Hi all,

We want to emphasise that a priority of the design is that it must look:
• Professional
• Sophisticated
Please do not hesitate to use completely different colour schemes to the ones that are on our website- as we have said, our website will change in the near future, so cohesion between the current project and the website is not necessary!

Thanks!

Thank you for your submissions so far. There are some great ideas hidden in there. 

An issue we are having is that most of you are conforming to the same understanding of what it should look like. Remember that there is NO NEED to be bound by the image of firm as is. That is, feel free to use a different colour logo.

For inspiration, we relate well to the design aesthetics of: http://www.tinfernstudio.co.uk/

Look forward to seeing your 'out of the box' submissions. 

Reason: We've received a large amount of fantastic designs. However, what we're really looking for is something original. Please feel free to think outside the box (the final design doesn't need to look like a print ad), and construct a design that is completely incongruous with our website! While we do appreciate a minimalistic design, we have yet to receive something that really grabs your attention with its visuals. We're not sure but this may or may not be achieved with a full colour design. Thanks for all your submissions- they all have some features that really click with us. We look forward to the next wave of submissions!

Target Market(s)

We have various target markets, including mainly families, elderly people, blue collar workers.

These are individuals who are looking for assistance. They feel helpless or wronged.

Keep in mind that the people accessing these are those who prefer going to a printed directory rather than using a google search.

Industry/Entity Type

Law Firm

Font styles to use
Serif
Sans Serif

Requirements
Must have
• - Our name 'Velbrook Compensation Lawyers'
- Our logo (attached as logo.eps, logo.png, and logo.tif)
- Must include phone number as 1300 XXX XXX (this must be prominent)
- Must include the following service areas in these words: Motor vehicle claims, medical claims, superannuation claims, Workplace claims, negligence claims
- Our email address: info@velbrooklegal.com.au
- Our website address: www.velbrooklegal.com.au
- The following catchphrases: '98% success rate', and 'No win no fee' in those words
- Our location '412 Carvel Lane, Smithville, SYDNEY'
- For sizing dimensions, we need one in 154mm x 118mm and also a design in 175mm x 113mm (B4 Half Page) [refer to pdf attached]
Nice to have
• - Text indicating free initial consulatation
- Professional colour scheme
- As our website will be changed, do not worry about making the advertisement cohesive with our website design
- We want the design to be modern, but still professional
- Clean typeface
- No gradient colour scheme
- When designing, if you are looking to place more text onto the advertisement, these may be some considerations (feel free to change the wording): Accredited specialists, home and hospital visits

```html
<!DOCTYPE html>
<html lang="en">
<head>
<meta charset="utf-8">
<title>Velbrook Compensation Lawyers – Directory Advertisements</title>
<link rel="stylesheet" href="https://fonts.googleapis.com/css2?family=Arimo:wght@400;700&family=Montserrat:wght@300&display=swap">
<style>
  :root {
    --orange: #f26f21;
    --orange-deep: #d9531a;
    --ink: #111111;
    --slate: #3d4347;
    --frame: #4a4a4a;
    --white: #ffffff;
    --sun: #e9ad34;
    --sun-soft: #f5d98a;
  }
  * { margin: 0; padding: 0; box-sizing: border-box; }
  html, body { width: 875px; height: 1200px; overflow: hidden; background: var(--white); }
  body { position: relative; font-family: "Arimo", Arial, sans-serif; color: var(--ink); }

  .ad { position: absolute; border: 3px solid var(--frame); background: var(--white); overflow: hidden; }
  .ad--half { left: 53px; top: 0; width: 767px; height: 588px; }
  .ad--wide { left: 0; top: 632px; width: 875px; height: 568px; }
  .ad > * { position: absolute; }

  .brand-mark { border-radius: 50%; background: var(--orange); width: 104px; height: 104px; }
  .brand-name { font-family: "Arimo", Arial, sans-serif; font-weight: 400; color: var(--slate); line-height: 1; white-space: nowrap; }
  .brand-name__title { display: block; font-size: 60px; letter-spacing: 5px; }
  .brand-name__sub { display: block; font-size: 16px; letter-spacing: 3.6px; margin-top: 12px; }

  .rule { left: 0; right: 0; background: var(--orange); }

  .hero-photo { left: 0; right: 0;
    background: linear-gradient(90deg, var(--sun) 0%, var(--sun-soft) 35%, #fbeccb 52%, var(--white) 68%); }

  .burst { width: 116px; height: 116px; }
  .burst__ray { position: absolute; left: 17px; top: 17px; width: 82px; height: 82px;
    background: radial-gradient(circle at 40% 35%, #f5893a, var(--orange-deep)); }
  .burst__ray:nth-child(2) { transform: rotate(22.5deg); }
  .burst__ray:nth-child(3) { transform: rotate(45deg); }
  .burst__ray:nth-child(4) { transform: rotate(67.5deg); }
  .burst__value { position: absolute; inset: 0; display: flex; align-items: center; justify-content: center;
    color: var(--white); font-weight: 700; font-size: 50px; letter-spacing: -2px; }
  .burst__value sup { font-size: 20px; align-self: flex-start; margin-top: 34px; margin-left: 2px; }

  .success { width: 140px; text-align: center; color: var(--orange); font-weight: 700; font-size: 25px; line-height: 30px; }

  .services { list-style: none; font-size: 23.5px; line-height: 39px; color: var(--ink); }
  .services li::before { content: ""; display: inline-block; width: 8px; height: 8px; border-radius: 50%;
    background: var(--orange); margin-right: 9px; vertical-align: middle; position: relative; top: -2px; }

  .no-win { background: var(--orange); border-radius: 10px; color: var(--white); font-weight: 700; font-size: 40px;
    display: flex; align-items: center; justify-content: center; letter-spacing: 0.5px;
    text-shadow: 1px 2px 2px rgba(0,0,0,0.3); box-shadow: 0 3px 5px rgba(0,0,0,0.25); }

  .consult { font-weight: 700; font-size: 20px; line-height: 30px; text-align: center; }
  .consult__free { color: var(--orange); font-size: 29px; margin-right: 8px; }

  .contact { left: 0; right: 0; bottom: 0; background: var(--orange); color: var(--white); font-weight: 700; }
  .contact > * { position: absolute; white-space: nowrap; }
  .contact__line { font-size: 20px; }
  .contact__phone { font-size: 45px; letter-spacing: 0.5px; }
  .contact__address { font-size: 14.5px; }
</style>
</head>
<body>

<section class="ad ad--half" aria-label="Half page advertisement, 154 by 118 mm">
  <div class="brand-mark" style="left:143px; top:11px;"></div>
  <div class="brand-name" style="left:270px; top:22px;">
    <span class="brand-name__title">VELBROOK</span>
    <span class="brand-name__sub">COMPENSATION LAWYERS</span>
  </div>
  <div class="rule" style="top:119px; height:6px;"></div>
  <div class="hero-photo" role="img" aria-label="Photo of a smiling woman in warm autumn sunlight" style="top:125px; height:377px;"></div>

  <div class="burst" style="left:331px; top:144px;">
    <span class="burst__ray"></span><span class="burst__ray"></span><span class="burst__ray"></span><span class="burst__ray"></span>
    <span class="burst__value">98<sup>%</sup></span>
  </div>
  <p class="success" style="left:319px; top:268px;">Success<br>Rate</p>

  <ul class="services" style="left:462px; top:145px;">
    <li>Motor Vehicle Claims</li>
    <li>Medical Claims</li>
    <li>Superannuation Claims</li>
    <li>Workplace Claims</li>
    <li>Negligence Claims</li>
  </ul>

  <div class="no-win" style="left:372px; top:349px; width:376px; height:68px;">NO WIN NO FEE</div>
  <p class="consult" style="left:470px; top:435px; width:220px;"><span class="consult__free">FREE</span>INITIAL<br>CONSULTATION</p>

  <div class="contact" style="height:80px;">
    <span class="contact__line" style="left:26px; top:16px;">info@velbrooklegal.com.au</span>
    <span class="contact__line" style="left:26px; top:52px;">www.velbrooklegal.com.au</span>
    <span class="contact__phone" style="left:397px; top:8px;">1300 482 317</span>
    <span class="contact__address" style="left:405px; top:57px;">412 Carvel Lane, Smithville, SYDNEY</span>
  </div>
</section>

<section class="ad ad--wide" aria-label="Half page advertisement, 175 by 113 mm">
  <div class="brand-mark" style="left:211px; top:15px;"></div>
  <div class="brand-name" style="left:343px; top:26px;">
    <span class="brand-name__title" style="font-size:62px;">VELBROOK</span>
    <span class="brand-name__sub">COMPENSATION LAWYERS</span>
  </div>
  <div class="rule" style="top:127px; height:7px;"></div>
  <div class="hero-photo" role="img" aria-label="Photo of a smiling woman in warm autumn sunlight" style="top:134px; height:338px;"></div>

  <div class="burst" style="left:399px; top:148px;">
    <span class="burst__ray"></span><span class="burst__ray"></span><span class="burst__ray"></span><span class="burst__ray"></span>
    <span class="burst__value">98<sup>%</sup></span>
  </div>
  <p class="success" style="left:387px; top:275px;">Success<br>Rate</p>

  <ul class="services" style="left:545px; top:150px;">
    <li>Motor Vehicle Claims</li>
    <li>Medical Claims</li>
    <li>Superannuation Claims</li>
    <li>Workplace Claims</li>
    <li>Negligence Claims</li>
  </ul>

  <div class="no-win" style="left:459px; top:350px; width:376px; height:70px;">NO WIN NO FEE</div>
  <p class="consult" style="left:449px; top:434px; width:400px; text-align:left;"><span class="consult__free">FREE</span>&nbsp;INITIAL CONSULTATION</p>

  <div class="contact" style="height:91px;">
    <span class="contact__line" style="left:61px; top:18px;">info@velbrooklegal.com.au</span>
    <span class="contact__line" style="left:61px; top:51px;">www.velbrooklegal.com.au</span>
    <span class="contact__phone" style="left:467px; top:8px;">1300 482 317</span>
    <span class="contact__address" style="left:477px; top:60px;">412 Carvel Lane, Smithville, SYDNEY</span>
  </div>
</section>

</body>
</html>
```